'Hold On Through Winter, Young Ones'

This 40 page booklet (A5 format = A4 page folded) is aimed at TEENAGERS at risk. New Zealand has a very high teen suicide rate, so this booklet cover design needs to be colorful, bold and evye catching for teenagers.

Target Market(s)

Teenagers

Industry/Entity Type

High School students

Requirements
Must have
• A colorful bold design to grab the attention of teens
Nice to have
• The cover could include a generic photo of a teen or group of teens, OR a stylised graphic
Should not have
• not too many words. Short author bio supplied on request: Marcus Thelwell had a difficult upbringing. He has battled low self-esteem and depression most of his life BUT he has always found a way through and learned to process the pain of bullying and abuse.'

```html
<!DOCTYPE html>
<html lang="en">
<head>
<meta charset="utf-8">
<title>Hold On Through Winter, Young Ones — Cover Spread</title>
<link href="https://fonts.googleapis.com/css2?family=Bebas+Neue&family=Poppins:wght@700;800&family=Roboto:wght@400&display=swap" rel="stylesheet">
<style>
  :root {
    --stage: #cfcfcf;
    --lilac: #c59dd2;
    --plum: #7a4a8e;
    --aubergine: #2c0a2e;
    --ink: #0b0b0b;
    --white: #ffffff;
    --cyan: #2fe6e6;
    --red: #d8343f;
    --sun-top: #9b6fb0;
    --sun-mid: #f0a54a;
    --sun-low: #b8452f;
  }
  * { box-sizing: border-box; margin: 0; padding: 0; }
  html, body { width: 1200px; height: 590px; overflow: hidden; background: var(--stage); }
  .spread {
    position: absolute; left: 196px; top: 10px;
    width: 807px; height: 570px; display: flex;
  }
  .back-cover {
    position: relative; width: 403px; height: 100%;
    background: linear-gradient(to bottom, var(--lilac) 0%, var(--lilac) 38%, var(--plum) 68%, var(--aubergine) 100%);
  }
  .blurb {
    position: absolute; left: 31px; top: 205px; width: 342px;
    font-family: "Roboto", Arial, sans-serif; font-size: 12.3px; line-height: 16.2px;
    color: var(--white); text-align: justify;
  }
  .barcode-space {
    position: absolute; left: 261px; top: 477px; width: 111px; height: 65px;
    background: var(--white);
  }
  .web-address {
    position: absolute; left: 31px; top: 533px;
    font-family: "Poppins", Arial, sans-serif; font-weight: 700; font-size: 10px;
    color: var(--white); letter-spacing: 0.3px;
  }
  .front-cover { position: relative; width: 404px; height: 100%; overflow: hidden; background: var(--ink); }
  .front-art { position: absolute; inset: 0; }
  .title {
    position: absolute; left: 0; top: 36px; width: 404px;
    font-family: "Bebas Neue", Impact, sans-serif; line-height: 0.86;
  }
  .title-lead { display: block; text-align: center; color: var(--white); font-size: 50px; }
  .title-main {
    display: block; text-align: center; color: var(--cyan); font-size: 96px;
    text-shadow: 3px 3px 0 var(--red);
  }
  .title-row { display: flex; align-items: center; justify-content: center; gap: 8px; }
  .title-row .title-main { font-size: 86px; }
  .title-tags { display: flex; flex-direction: column; gap: 6px; }
  .tag {
    background: var(--red); color: var(--white); font-family: "Poppins", Arial, sans-serif;
    font-weight: 800; font-size: 17px; line-height: 1; padding: 4px 6px 3px; transform: rotate(-2deg);
  }
  .author {
    position: absolute; left: 0; width: 404px; top: 520px; text-align: center;
    font-family: "Poppins", Arial, sans-serif; font-weight: 800; font-size: 22px;
    letter-spacing: 2px; color: var(--white);
  }
</style>
</head>
<body>
  <main class="spread">
    <section class="back-cover">
      <p class="blurb">Life is hard. Life is a struggle. But if you look anywhere in the animal kingdom (and humans are animals) you will see that most animals struggle to survive. How does a baby bird escape the egg shell? Struggle. How does a baby animal escape the prison of its mother's womb? Pain, trauma and struggle. Pain and struggle are a normal part of life. The sooner we realise and accept this, the easier it will be to grow strategies TO COPE WITH LIFE. To process the pain of this life. To be better equipped to deal with the challenges and realities of this one life we've been gifted.</p>
      <div class="barcode-space"></div>
      <p class="web-address">WWW.STEADYGROUND.NZ</p>
    </section>

    <section class="front-cover">
      <svg class="front-art" width="404" height="570" viewBox="0 0 404 570">
        <defs>
          <linearGradient id="sunsetFill" x1="0" y1="0" x2="0" y2="1">
            <stop offset="0" stop-color="var(--sun-top)"/>
            <stop offset="0.45" stop-color="var(--sun-mid)"/>
            <stop offset="0.8" stop-color="var(--sun-low)"/>
            <stop offset="1" stop-color="#2a1010"/>
          </linearGradient>
        </defs>
        <rect class="sky-base" x="0" y="0" width="404" height="570" fill="var(--lilac)"/>
        <rect class="group-photo" role="img" aria-label="Photo: silhouettes of a group of teenagers jumping against a sunset over hills" x="0" y="250" width="404" height="260" fill="url(#sunsetFill)"/>
        <path class="brush-band" fill="var(--ink)" d="M38 0 L360 0 L372 8 L404 4 L404 230 L380 236 L330 262 L300 268 L250 300 L210 320 L150 336 L90 350 L40 352 L20 345 L34 320 L16 300 L30 276 L24 250 L10 230 L28 205 L14 180 L40 160 L30 130 L44 110 L22 90 L40 70 L30 45 L46 24 Z"/>
        <path class="brush-fleck" fill="var(--lilac)" d="M360 0 L404 0 L404 6 L380 12 Z"/>
        <rect class="footer-band" x="0" y="505" width="404" height="65" fill="var(--ink)"/>
      </svg>
      <h1 class="title">
        <span class="title-lead">HOLD ON</span>
        <span class="title-main">THROUGH</span>
        <span class="title-row">
          <span class="title-main">WINTER</span>
          <span class="title-tags"><span class="tag">YOUNG</span><span class="tag">ONES</span></span>
        </span>
      </h1>
      <p class="author">MARCUS THELWELL</p>
    </section>
  </main>
</body>
</html>
```